Sophrologist needs a cool signage at door entrance

I need signage for dr in sophrology based in Belgium (french speaking). The signed should capture the name the "Mireille Vantoorn" - "Naturopathe-Sophrologue-Reiki" and a catchphrase = (Healthy way of life)
« Fais du bien à ton corps, pour que ton âme ait envie d’y rester »
Requirements
Must have
- Hey,
Thats the instagram account for some inspiration www.instagram.com/mireille_serene_wellbeing
Light colors, green, blue
Healthy way of life
Size is 45cm wide on 30 cm high
The signage will be placed in front off woof pannel

```html
<!DOCTYPE html>
<html lang="fr">
<head>
<meta charset="utf-8">
<title>Mireille Vantoorn – Enseigne</title>
<link rel="stylesheet" href="https://fonts.googleapis.com/css2?family=Tinos:wght@700&family=Sacramento&display=swap">
<style>
  :root {
    --backdrop: #e4e5e7;
    --sky: #dbeff9;
    --teal: #3e8f86;
    --ink: #1c1c1c;
    --white: #ffffff;
    --leaf-deep: #2f7f78;
    --leaf-soft: #8fbf9a;
  }
  * { margin: 0; padding: 0; box-sizing: border-box; }
  html, body {
    width: 1200px;
    height: 942px;
    overflow: hidden;
    background: var(--backdrop);
  }
  .sign {
    position: absolute;
    left: 122px;
    top: 160px;
    width: 952px;
    height: 635px;
    background: var(--sky);
    overflow: hidden;
  }
  .sign-wave {
    position: absolute;
    inset: 0;
    width: 952px;
    height: 635px;
  }
  .foliage {
    position: absolute;
    border-radius: 50%;
    opacity: 0.75;
  }
  .foliage--top {
    left: 18px;
    top: -20px;
    width: 210px;
    height: 260px;
    background: radial-gradient(ellipse at 50% 45%, var(--leaf-deep) 0%, var(--leaf-soft) 45%, rgba(143,191,154,0) 72%);
  }
  .foliage--bottom {
    left: 826px;
    top: 480px;
    width: 140px;
    height: 170px;
    background: radial-gradient(ellipse at 50% 50%, var(--leaf-soft) 0%, var(--leaf-deep) 40%, rgba(62,143,134,0) 72%);
  }
  .name {
    position: absolute;
    left: 0;
    width: 100%;
    top: 42px;
    text-align: center;
    font-family: "Tinos", "Times New Roman", serif;
    font-weight: 700;
    font-size: 62px;
    line-height: 55px;
    color: var(--teal);
  }
  .name-rule {
    position: absolute;
    left: 416px;
    top: 171px;
    width: 120px;
    height: 4px;
    background: var(--teal);
  }
  .roles {
    position: absolute;
    left: 0;
    width: 100%;
    top: 200px;
    text-align: center;
    font-family: "Tinos", "Times New Roman", serif;
    font-weight: 700;
    font-size: 25px;
    line-height: 1;
    color: var(--ink);
  }
  .roles .dot { color: var(--teal); padding: 0 4px; }
  .motto {
    position: absolute;
    left: 0;
    width: 100%;
    top: 262px;
    text-align: center;
    font-family: "Sacramento", cursive;
    font-size: 116px;
    letter-spacing: 3px;
    line-height: 1;
    color: var(--ink);
  }
  .tagline {
    position: absolute;
    left: 0;
    width: 100%;
    top: 534px;
    text-align: center;
    font-family: "Tinos", "Times New Roman", serif;
    font-weight: 700;
    font-size: 31px;
    line-height: 37px;
    color: var(--white);
  }
</style>
</head>
<body>
  <div class="sign">
    <svg class="sign-wave" viewBox="0 0 952 635" aria-hidden="true">
      <path fill="var(--white)" d="M54 452 C120 492 170 508 238 508 C400 508 560 432 718 430 C820 430 900 452 952 476 L952 635 L0 635 L0 456 Z"/>
      <path fill="var(--teal)" d="M54 450 C120 482 170 496 238 496 C400 496 560 412 718 412 C820 412 900 440 952 470 L952 476 C900 452 820 430 718 430 C560 432 400 508 238 508 C170 508 120 492 54 452 Z"/>
      <path fill="var(--teal)" d="M0 456 C80 492 160 518 238 518 C400 518 560 448 718 448 C820 448 900 468 952 486 L952 635 L0 635 Z"/>
    </svg>

    <div class="foliage foliage--top" role="img" aria-label="Watercolour eucalyptus leaves in teal and soft green"></div>
    <div class="foliage foliage--bottom" role="img" aria-label="Watercolour eucalyptus leaves in teal and soft green"></div>

    <h1 class="name">MIREILLE<br>VANTOORN</h1>
    <div class="name-rule"></div>
    <p class="roles">NATUROPATHE<span class="dot">•</span>SOPHROLOGUE<span class="dot">•</span>REIKI</p>
    <p class="motto">Healthy way of life</p>
    <p class="tagline">FAIS DU BIEN À TON CORPS,<br>POUR QUE TON ÂME AIT ENVIE D’Y RESTER</p>
  </div>
</body>
</html>
```